Construction Company

I'm a new construction company called Kelden Construction. I want my card to look simple and clean. I have provided a sample of what I want the front to look like (Kelden_Card.jpeg) and a back ground for the back of the (Kelden_Card_Background.jpeg) - the background can be faded so my name and other information is more prominent.
Construction

```html
<!DOCTYPE html>
<html lang="en">
<head>
<meta charset="utf-8">
<title>Kelden Construction – Business Card</title>
<link href="https://fonts.googleapis.com/css2?family=Open+Sans:wght@400;600;700&display=swap" rel="stylesheet">
<style>
  :root {
    --stage: #1e1e1f;
    --card-navy: #2b3a4d;
    --card-navy-deep: #223042;
    --blueprint-line: #34465c;
    --accent-orange: #f0990f;
    --text-light: #e6e9ee;
    --text-muted: #9aa5b3;
  }
  * { box-sizing: border-box; margin: 0; padding: 0; }
  html, body {
    width: 1200px; height: 900px; overflow: hidden;
    background: var(--stage);
    font-family: "Open Sans", Arial, sans-serif;
  }
  .canvas {
    position: relative; width: 1200px; height: 900px;
    display: flex; flex-direction: column; align-items: center;
    justify-content: center; gap: 40px;
  }
  .card {
    position: relative; width: 700px; height: 400px;
    background: var(--card-navy); overflow: hidden;
    box-shadow: 0 10px 30px rgba(0,0,0,.5);
  }
  /* Front */
  .card-front .wordmark {
    position: absolute; left: 0; right: 0; top: 118px;
    text-align: center; color: var(--accent-orange);
    font-weight: 700; font-size: 64px; line-height: 1.05;
    letter-spacing: -0.5px;
  }
  .card-front .website {
    position: absolute; left: 0; right: 0; top: 322px;
    text-align: center; color: var(--accent-orange);
    font-size: 15px; letter-spacing: .3px;
  }
  /* Back */
  .card-back .blueprint {
    position: absolute; inset: 0;
    background: linear-gradient(135deg, var(--card-navy-deep) 0%, var(--blueprint-line) 50%, var(--card-navy-deep) 100%);
    opacity: .55;
  }
  .card-back .person {
    position: absolute; right: 60px; top: 40px; text-align: left;
  }
  .card-back .person-name {
    color: var(--accent-orange); font-weight: 700; font-size: 20px;
  }
  .card-back .person-role {
    color: var(--text-light); font-weight: 600; font-size: 15px;
    padding-left: 34px; margin-top: -2px;
  }
  .card-back .address {
    position: absolute; right: 40px; top: 178px; text-align: right;
    color: var(--text-muted); font-size: 17px; line-height: 1.3;
    font-style: normal;
  }
  .card-back .contacts {
    position: absolute; left: 40px; bottom: 38px; list-style: none;
    color: var(--text-light); font-size: 19px; line-height: 1.35;
  }
  .card-back .contacts li { display: flex; align-items: center; gap: 10px; }
  .card-back .contacts svg { width: 18px; height: 18px; fill: var(--accent-orange); flex: none; }
</style>
</head>
<body>
<main class="canvas">
  <section class="card card-front" aria-label="Card front">
    <p class="wordmark">Kelden<br>Construction</p>
    <p class="website">www.keldenconstruction.com</p>
  </section>

  <section class="card card-back" aria-label="Card back">
    <div class="blueprint" role="img" aria-label="Faded architectural floor plan background"></div>
    <div class="person">
      <p class="person-name">Marcus Holloway</p>
      <p class="person-role">managing director</p>
    </div>
    <address class="address">48 Harbor Lane<br>Millbrook, New York<br>12601</address>
    <ul class="contacts">
      <li>
        <svg viewBox="0 0 18 18" aria-hidden="true"><path d="M5 1h8a1 1 0 0 1 1 1v14a1 1 0 0 1-1 1H5a1 1 0 0 1-1-1V2a1 1 0 0 1 1-1zm1 2v10h6V3zm3 11.2a.9.9 0 1 0 0 1.8.9.9 0 0 0 0-1.8z"/></svg>
        555 214 36 90
      </li>
      <li>
        <svg viewBox="0 0 18 18" aria-hidden="true"><path d="M5 2h8v4H5zM2 7h14a1 1 0 0 1 1 1v6h-3v2H4v-2H1V8a1 1 0 0 1 1-1zm4 5v3h6v-3z"/></svg>
        555 307 48 12
      </li>
      <li>
        <svg viewBox="0 0 18 18" aria-hidden="true"><path d="M1 4h16v10H1zm1.5 1.2L9 10l6.5-4.8z"/></svg>
        mholloway@keldenconstruction.com
      </li>
    </ul>
  </section>
</main>
</body>
</html>
```